World Wide News and Current Affairs website

We intends to start up a new website which deals on New and Current Affairs.
Attention Designers,
We want a home page design for this project. Our business is based in the United States. Our goal is to become a well known brand.
The website would consist of a category for News, Business and Tech.
The theme should be beautiful and attention seeking. The website would take bulk of it's news from the US, and Europe.
Designers can get inspiration from already existing new websites such as HVZ, FQJ, DORNAKE.
All designs should be clean and easy to navigate.

```html
<!DOCTYPE html>
<html lang="en">
<head>
<meta charset="utf-8">
<title>World Wide News — Home</title>
<link rel="stylesheet" href="https://fonts.googleapis.com/css2?family=Roboto+Condensed:wght@400;700&family=Roboto:wght@400;500;700&display=swap">
<style>
:root{
  --red:#e42b2b;
  --ink:#1b1b1f;
  --dark:#1f1f24;
  --panel:#2a2a31;
  --grey-bg:#ececec;
  --white:#ffffff;
  --muted:#8b8b93;
  --text:#3a3a40;
  --head:"Roboto Condensed",Arial,sans-serif;
  --body:"Roboto",Arial,sans-serif;
}
*{box-sizing:border-box;margin:0;padding:0}
html,body{width:1200px;height:3448px;overflow:hidden}
body{position:relative;background:var(--grey-bg);font-family:var(--body);color:var(--text)}
.abs{position:absolute}
.ph{position:absolute}
.topbar{left:0;top:0;width:1200px;height:41px;background:var(--ink);color:#cfcfd4;font-size:11px}
.logo{position:absolute;left:0;top:0;width:82px;height:41px;background:var(--red);color:#fff;font:700 18px/41px var(--head);text-align:center;letter-spacing:1px}
.follow{position:absolute;left:100px;top:0;line-height:41px;display:flex;align-items:center;gap:9px}
.dot{width:9px;height:9px;border-radius:50%;background:#8a8a92;display:inline-block}
.dot.red{background:var(--red)}
.topnav{position:absolute;right:14px;top:0;line-height:41px;display:flex;gap:20px;align-items:center}
.topnav b{color:#fff;font-weight:500}
.tag{font:700 10px var(--head);letter-spacing:.5px;text-transform:uppercase;color:#fff;display:flex;align-items:center;gap:6px}
.tag::before{content:"";width:3px;height:10px;background:var(--red)}
.tag.dark{color:#555}
.title{font-family:var(--head);font-weight:700;text-transform:uppercase;line-height:1.2}
.meta{font-size:9px;color:#bbb;display:flex;gap:12px;align-items:center}
.meta.dark{color:#888}
.meta i{display:inline-block;width:8px;height:6px;border:1px solid currentColor;border-radius:50%;margin-right:3px;vertical-align:middle}
.meta i.c{border-radius:1px}
.hero-story{position:absolute;overflow:hidden}
.hero-story .cap{position:absolute;left:28px;right:28px;bottom:22px}
.hero-story .title{color:#fff;margin:8px 0 10px}
.bubble{position:absolute;width:34px;height:34px;border-radius:50%;background:var(--red);box-shadow:0 0 0 4px #fff}
.bubble svg{position:absolute;left:10px;top:10px}
.card{position:absolute;background:var(--white);overflow:hidden}
.card .body{padding:14px 16px}
.card .title{color:#222;font-size:13px;margin:8px 0 10px}
.quote{background:linear-gradient(135deg,#2b2e3a,#3d4150);color:#fff}
.btn{position:absolute;background:var(--red);color:#fff;font:700 10px var(--body);padding:5px 10px}
.player{position:absolute;left:0;right:0;bottom:0;height:34px;background:linear-gradient(transparent,rgba(0,0,0,.75))}
.player .play{position:absolute;left:12px;top:12px;width:0;height:0;border-left:9px solid #fff;border-top:6px solid transparent;border-bottom:6px solid transparent}
.player .bar{position:absolute;left:30px;right:70px;top:17px;height:2px;background:rgba(255,255,255,.35)}
.player .bar::before{content:"";position:absolute;left:0;top:0;height:2px;width:28%;background:var(--red)}
.player .ctl{position:absolute;right:12px;top:12px;display:flex;gap:6px}
.player .ctl span{width:9px;height:9px;border:1.5px solid #fff;border-radius:2px}
.share{position:absolute;right:12px;top:12px;width:20px;height:20px;border-radius:50%;background:rgba(255,255,255,.85)}
.videos{left:0;top:2157px;width:1200px;height:350px;background:var(--dark)}
.vhead{position:absolute;top:38px;font:700 12px var(--head);color:#fff;text-transform:uppercase;display:flex;gap:8px;align-items:center}
.vhead::before{content:"";width:8px;height:8px;background:var(--red)}
.vcap{position:absolute;top:296px;font-size:9px;color:#9a9aa2}
.app{left:0;top:2518px;width:1200px;height:70px;background:var(--red);color:#fff}
.app-name{position:absolute;left:22px;top:24px;display:flex;align-items:center;gap:8px;font:700 18px/22px var(--head);color:#fff}
.app-name::before{content:"";width:14px;height:14px;background:#fff}
.about{left:0;top:2599px;width:1200px;height:496px;background:linear-gradient(180deg,#2e2f36,#24252b)}
.about p,.rcard p{font-size:9px;line-height:1.55}
.stat{position:absolute;top:452px;display:flex;align-items:center;gap:8px;color:#fff;font:700 14px var(--head)}
.stat span{width:22px;height:22px;border-radius:50%;background:var(--red)}
.special{left:0;top:3128px;width:1200px;height:58px;background:#222227}
.special .lbl{position:absolute;left:0;top:0;width:100px;height:58px;background:var(--red);color:#fff;font:700 12px/1.2 var(--head);padding:15px 12px;text-transform:uppercase}
.special .item{position:absolute;top:0;height:58px;padding:16px 18px;color:#fff;font:700 11px/1.25 var(--head);text-transform:uppercase;width:265px}
.footer{left:0;top:3196px;width:1200px;height:220px;background:var(--ink)}
.fcol{position:absolute;top:22px;width:90px}
.fcol h4{font:700 13px var(--head);color:#fff;margin-bottom:12px;text-transform:uppercase}
.fcol a{display:block;font-size:9px;color:#8d8d95;line-height:1.75;text-decoration:none}
.fcol a.on{color:var(--red)}
.bottombar{left:0;top:3416px;width:1200px;height:32px;background:#141417}
.dropcap{float:left;width:26px;height:26px;background:#222;color:#fff;font:700 18px/26px var(--head);text-align:center;margin:2px 8px 2px 0}
</style>
</head>
<body>

<header class="abs topbar">
  <div class="logo">LOGO</div>
  <div class="follow">Follow Us <span class="dot"></span><span class="dot red"></span><span class="dot"></span><span class="dot"></span><span class="dot"></span></div>
  <nav class="topnav">
    <span>Monday, Aug 17, 2015</span><b>Projects</b><b>About Us</b><b>Investigations</b><b>Tags</b><b>RSS</b><b>Subscribe</b>
    <svg width="12" height="12" viewBox="0 0 12 12"><circle cx="5" cy="5" r="3.6" fill="none" stroke="#fff" stroke-width="1.5"/><line x1="7.6" y1="7.6" x2="11" y2="11" stroke="#fff" stroke-width="1.5"/></svg>
  </nav>
</header>

<section class="hero-story" style="left:0;top:41px;width:598px;height:599px;background:linear-gradient(160deg,#3b3b41 0%,#1e1e22 60%,#121215 100%)" role="img" aria-label="Politician speaking at a microphone">
  <div class="cap">
    <div class="tag">Politics</div>
    <h2 class="title" style="font-size:24px;max-width:520px">U.S. House chamber closed after unknown material</h2>
    <div class="meta">August 6, 2015 <span><i></i>1456</span><span><i class="c"></i>32</span></div>
  </div>
</section>
<section class="hero-story" style="left:602px;top:41px;width:598px;height:299px;background:linear-gradient(135deg,#5a6a8c,#2e3550 55%,#6b7080)" role="img" aria-label="Football players in blue helmets on the field">
  <div class="cap">
    <div class="tag">Sports</div>
    <h2 class="title" style="font-size:20px;max-width:420px">Philip Rowan: I'm going to be a charger, wherever we are</h2>
    <div class="meta">August 6, 2015 <span><i></i>1456</span><span><i class="c"></i>32</span></div>
  </div>
</section>
<section class="hero-story" style="left:602px;top:344px;width:296px;height:296px;background:linear-gradient(160deg,#6d4a4a,#2d2a33 60%,#1b1b20)" role="img" aria-label="Flag with a soldier in front">
  <div class="cap">
    <div class="tag">Money</div>
    <h2 class="title" style="font-size:18px">U.S. flag raised over embassy in Republic of Cuba</h2>
    <div class="meta">August 6, 2015 <span><i></i>1456</span><span><i class="c"></i>32</span></div>
  </div>
</section>
<section class="hero-story" style="left:902px;top:344px;width:298px;height:296px;background:linear-gradient(160deg,#7a4a3a,#3a2a28 60%,#1b1b20)" role="img" aria-label="Firefighter at a port blast site">
  <div class="cap">
    <div class="tag">World</div>
    <h2 class="title" style="font-size:18px">Death toll in Chinese port blasts rises to 104</h2>
    <div class="meta">August 6, 2015 <span><i></i>1456</span><span><i class="c"></i>32</span></div>
  </div>
</section>
<div class="bubble" style="left:583px;top:623px"><svg width="14" height="14" viewBox="0 0 14 14"><path d="M11 7a4 4 0 1 1-1.2-2.9" fill="none" stroke="#fff" stroke-width="1.8"/><path d="M10 1v3.5H6.5" fill="none" stroke="#fff" stroke-width="1.8"/></svg></div>

<article class="card" style="left:7px;top:655px;width:287px;height:288px">
  <div class="body">
    <div class="tag dark">Politics</div>
    <h3 class="title" style="max-width:160px">Sticky post: Jed Barsh overhaul</h3>
    <div class="meta dark">August 6, 2015 <span><i></i>1456</span><span><i class="c"></i>32</span></div>
    <p style="font-size:9px;line-height:1.55;margin-top:14px;color:#555"><span class="dropcap">P</span>Praesent adipiscing. Phasellus ullamcorper ipsum rutrum nunc. Nunc nonummy metus. Vestibulum volutpat pretium libero. Cras id dui. Aenean ut eros et nisl sagittis vestibulum. Nullam nulla eros, ultricies sit amet, nonummy id, imperdiet feugiat, pede. Sed lectus. Donec mollis hendrerit risus. Phasellus nec sem in justo pellentesque facilisis. Etiam imperdiet imperdiet orci. Nunc nec neque. Phasellus leo dolor. <span style="color:var(--red)">Read More ›</span></p>
  </div>
  <ul style="position:absolute;left:196px;top:14px;width:84px;background:#fff;box-shadow:0 2px 8px rgba(0,0,0,.18);list-style:none;font-size:8px;color:#999">
    <li style="padding:6px 10px;border-bottom:1px solid #eee">Friendwall</li>
    <li style="padding:6px 10px;border-bottom:1px solid #eee">Chirper</li>
    <li style="padding:6px 10px;border-bottom:1px solid #eee">Circlr</li>
    <li style="padding:6px 10px;border-bottom:1px solid #eee">Pinboardy</li>
    <li style="padding:6px 10px">Careernet</li>
  </ul>
</article>

<article class="card" style="left:306px;top:655px;width:287px;height:587px">
  <div class="ph" style="left:0;top:0;width:287px;height:472px;background:linear-gradient(180deg,#8fc0e6,#b9d8ef 55%,#7f8a80)" role="img" aria-label="Statue of Liberty against a blue sky"></div>
  <div class="body" style="position:absolute;top:478px">
    <div class="tag dark">Money</div>
    <h3 class="title">Woman finds 4 urns in recently purchased used car</h3>
    <div class="meta dark">August 6, 2015 <span><i></i>1456</span><span><i class="c"></i>32</span></div>
  </div>
</article>

<article class="card quote" style="left:607px;top:655px;width:587px;height:288px">
  <div style="position:absolute;left:0;right:0;top:40px;text-align:center;font:700 36px var(--head);color:#fff">&rdquo;</div>
  <p class="title" style="position:absolute;left:60px;right:60px;top:95px;text-align:center;font-size:20px;color:#fff">Many men go fishing all of their lives without knowing that it is not fish they are after.</p>
  <div style="position:absolute;left:40px;top:215px;width:36px;height:36px;border-radius:50%;background:#6b6f80" role="img" aria-label="Author avatar"></div>
  <div style="position:absolute;left:86px;top:217px;font-size:9px;color:#ccc;width:240px"><b style="color:#fff">Orlando Ricky</b><br>Praesent adipiscing. Phasellus ullamcorper ipsum nunc. Nunc nonummy metus. Vestibulum volutpat libero.</div>
  <div style="position:absolute;right:40px;top:222px"><div class="tag">Sports</div><div class="meta" style="margin-top:6px">August 6, 2015 <span><i></i>156</span><span><i class="c"></i>32</span></div></div>
</article>

<article class="card" style="left:7px;top:955px;width:287px;height:287px">
  <div class="ph" style="left:0;top:0;width:287px;height:172px;background:linear-gradient(135deg,#4a5568,#2a2f3a 60%,#8b8f99)" role="img" aria-label="Two police officers"></div>
  <div class="body" style="position:absolute;top:178px">
    <div class="tag dark">Politics</div>
    <h3 class="title">What happened this week? Take our weekly news quiz</h3>
    <div class="meta dark">August 6, 2015 <span><i></i>156</span><span><i class="c"></i>32</span></div>
  </div>
</article>

<section class="hero-story" style="left:607px;top:955px;width:587px;height:586px;background:linear-gradient(90deg,#2b2a30 0%,#4a3a36 35%,#c29a86 65%,#e2cbbd 100%)" role="img" aria-label="Portrait of a woman with red lipstick">
  <div style="position:absolute;left:20px;top:320px;width:110px">
    <div class="tag">World</div>
    <h2 class="title" style="font-size:22px;color:#fff;margin:8px 0 10px">Interview with Lia Esheley about political issues in U.S.A</h2>
    <div class="meta">August 6, 2015 <span><i></i>1456</span></div>
  </div>
</section>

<article class="card" style="left:7px;top:1254px;width:287px;height:287px">
  <div class="ph" style="left:0;top:0;width:287px;height:172px;background:linear-gradient(135deg,#d8d8dc,#8a9ab5 50%,#b94a4a)" role="img" aria-label="Fans in patriotic costume"></div>
  <div class="body" style="position:absolute;top:178px">
    <div class="tag dark">Sports</div>
    <h3 class="title">Tiger tracker: Wynfield Championship, round 2</h3>
    <div class="meta dark">August 6, 2015 <span><i></i>156</span><span><i class="c"></i>32</span></div>
  </div>
</article>

<section class="hero-story" style="left:306px;top:1254px;width:287px;height:287px;background:linear-gradient(160deg,#6a6a72,#2c2c33 60%,#1a1a1f)" role="img" aria-label="Weightlifter in a gym">
  <div style="position:absolute;left:22px;top:125px;right:22px">
    <div class="tag">Sports</div>
    <h3 class="title" style="font-size:13px;color:#fff;margin-top:8px">Daniel Lettner has OpenWheel title within reach with Grant Rahman</h3>
  </div>
  <div style="position:absolute;left:22px;top:215px;display:flex;gap:6px">
    <span style="width:42px;height:30px;background:#555;border:2px solid var(--red)"></span><span style="width:42px;height:30px;background:#666"></span><span style="width:42px;height:30px;background:#4a4a52"></span><span style="width:42px;height:30px;background:#5a5a62"></span>
  </div>
  <span style="position:absolute;left:4px;top:218px;width:14px;height:24px;background:var(--red)"></span>
  <span style="position:absolute;right:4px;top:218px;width:14px;height:24px;background:var(--red)"></span>
</section>

<section class="hero-story" style="left:7px;top:1557px;width:586px;height:283px;background:linear-gradient(135deg,#b8bec8,#7e8896 55%,#5a6270)" role="img" aria-label="Fighter jet in flight, video">
  <span class="btn" style="left:12px;top:12px">Read More ›</span>
  <span class="share"></span>
  <div class="player"><span class="play"></span><span class="bar"></span><span class="ctl"><span></span><span></span></span></div>
</section>

<article class="card" style="left:607px;top:1557px;width:288px;height:283px">
  <div class="ph" style="left:0;top:0;width:288px;height:176px;background:linear-gradient(135deg,#6b4a3a,#c7783c 45%,#3a2e2a)" role="img" aria-label="Welder with sparks"></div>
  <div class="body" style="position:absolute;top:180px">
    <div class="tag dark">World</div>
    <h3 class="title" style="font-size:12px">Autopsy: St. Louis man killed by police was shot in back</h3>
    <div class="meta dark">August 6, 2015 <span><i></i>156</span><span><i class="c"></i>32</span></div>
  </div>
</article>

<article class="card" style="left:906px;top:1557px;width:288px;height:593px">
  <div class="ph" style="left:0;top:0;width:288px;height:467px;background:linear-gradient(180deg,#c9c0b3,#8a7b6a 50%,#3a3330)" role="img" aria-label="Bridge seen from a city street"></div>
  <div class="body" style="position:absolute;top:474px">
    <div class="tag dark">Money</div>
    <h3 class="title" style="font-size:12px">Blind teen with autism rocks star-spangled banner</h3>
    <div class="meta dark">August 6, 2015 <span><i></i>156</span><span><i class="c"></i>32</span></div>
  </div>
</article>

<section class="hero-story" style="left:7px;top:1856px;width:287px;height:294px;background:linear-gradient(180deg,#3a4050,#23252d 55%,#1a1b20)" role="img" aria-label="Capitol building at dusk">
  <div style="position:absolute;left:18px;top:112px;right:18px">
    <div class="tag">Politics</div>
    <h3 class="title" style="font-size:12px;color:#fff;margin-top:8px">Deadly infections from medical scopes go unreported, raising health risks</h3>
  </div>
  <div style="position:absolute;left:18px;top:230px;display:flex;gap:14px;font-size:9px;color:#ccc">
    <svg width="14" height="14" viewBox="0 0 14 14"><path d="M6 8l2-2M5 6l-2 2a2 2 0 0 0 3 3l2-2M9 8l2-2a2 2 0 0 0-3-3L6 5" fill="none" stroke="#fff" stroke-width="1.5"/></svg>
    <span>Download the full list of the richest people in<br>the world here</span>
  </div>
</section>

<article class="card" style="left:306px;top:1856px;width:589px;height:294px">
  <div class="ph" style="left:0;top:0;width:589px;height:168px;background:linear-gradient(135deg,#d5d5d8,#9a9aa0 50%,#4a4a50)" role="img" aria-label="Firefighters in smoke"></div>
  <div class="body" style="position:absolute;top:174px">
    <div class="tag dark">World</div>
    <h3 class="title" style="font-size:12px">Whale photobombs TV host complaining about not seeing any whales</h3>
    <div class="meta dark">August 6, 2015 <span><i></i>156</span><span><i class="c"></i>32</span></div>
  </div>
  <span class="btn" style="left:262px;top:236px">Load More</span>
</article>
<div class="bubble" style="left:583px;top:2130px"><svg width="14" height="14" viewBox="0 0 14 14"><path d="M11 7a4 4 0 1 1-1.2-2.9" fill="none" stroke="#fff" stroke-width="1.8"/><path d="M10 1v3.5H6.5" fill="none" stroke="#fff" stroke-width="1.8"/></svg></div>

<section class="abs videos">
  <div class="vhead" style="left:14px">50 Percent Off</div>
  <div class="vhead" style="left:313px">Productive Morning</div>
  <div class="vhead" style="left:614px">City Nights</div>
  <div class="vhead" style="left:913px">Beautiful Glass Lamp</div>
  <div class="hero-story" style="left:7px;top:62px;width:287px;height:218px;background:linear-gradient(135deg,#9a9a9e,#5a5a60)" role="img" aria-label="Sale sign, video"><span class="share"></span><div class="player"><span class="play"></span><span class="bar"></span><span class="ctl"><span></span><span></span></span></div></div>
  <div class="hero-story" style="left:306px;top:62px;width:287px;height:218px;background:linear-gradient(135deg,#8a8a90,#3e3e44)" role="img" aria-label="Hands typing on a keyboard, video"><span class="share"></span><div class="player"><span class="play"></span><span class="bar"></span><span class="ctl"><span></span><span></span></span></div></div>
  <div class="hero-story" style="left:607px;top:62px;width:288px;height:218px;background:linear-gradient(135deg,#6a5a70,#2c2438 60%,#b06a4a)" role="img" aria-label="City street at night, video"><span class="share"></span><div class="player"><span class="play"></span><span class="bar"></span><span class="ctl"><span></span><span></span></span></div></div>
  <div class="hero-story" style="left:906px;top:62px;width:288px;height:218px;background:radial-gradient(circle at 45% 45%,#f5d08a,#8a6a4a 40%,#3a3034)" role="img" aria-label="Glowing glass lamp, video"><span class="share"></span><div class="player"><span class="play"></span><span class="bar"></span><span class="ctl"><span></span><span></span></span></div></div>
  <div class="vcap" style="left:14px">Curabitur blandit mollis lacus. Nam adipiscing eleifend</div>
  <div class="vcap" style="left:313px">Cum sociis natoque penatibus et magnis morte</div>
  <div class="vcap" style="left:614px">Maecenas nec odio et ante tincidunt tempus</div>
  <div class="vcap" style="left:913px">Fusce vulputate eleifend purus scelerisque</div>
</section>

<section class="abs app">
  <div class="app-name">WWN</div>
  <h3 class="title" style="position:absolute;left:96px;top:14px;font-size:15px">Try our mobile app on Verdant or Pomeo</h3>
  <p style="position:absolute;left:96px;top:36px;width:1060px;font-size:8px;line-height:1.5;color:#ffe3e3">Aenean commodo ligula eget dolor. Aenean massa. Cum sociis natoque penatibus et magnis dis parturient montes, nascetur ridiculus mus. Donec quam felis, ultricies nec, pellentesque eu, pretium quis, sem. Nulla consequat massa quis enim. Donec pede justo, fringilla vel, aliquet nec, vulputate eget, arcu. In enim justo, rhoncus ut, imperdiet a, venenatis vitae, justo. Nullam dictum felis eu pede mollis pretium. Integer tincidunt. Cras dapibus vivamus elementum semper nisi aenean vulputate eleifend tellus.</p>
  <svg style="position:absolute;right:18px;top:14px" width="10" height="10" viewBox="0 0 10 10"><path d="M1 1l8 8M9 1l-8 8" stroke="#fff" stroke-width="2"/></svg>
</section>

<section class="abs about">
  <h2 class="title" style="position:absolute;left:40px;top:26px;font-size:30px;color:#fff">About us</h2>
  <span class="btn" style="left:718px;top:34px">Contact Us</span>
  <div class="ph" style="left:24px;top:92px;width:140px;height:150px;background:linear-gradient(135deg,#8a8a90,#3a3a40)" role="img" aria-label="Busy city street"></div>
  <p style="position:absolute;left:174px;top:92px;width:360px;color:#c7c7cd">Phasellus tempus. Proin viverra, ligula sit amet ultrices semper, ligula arcu tristique sapien, a accumsan nisi mauris ac eros. Donec vitae sapien ut libero venenatis faucibus. Nullam quis ante. Etiam sit amet orci eget eros faucibus tincidunt. Duis leo. Sed fringilla mauris sit amet nibh. Donec sodales sagittis magna. Sed consequat, leo eget bibendum sodales, augue velit cursus nunc, quis gravida magna mi a libero. Fusce vulputate eleifend sapien. Vestibulum purus quam, scelerisque ut, mollis sed, nonummy id, metus. Nullam accumsan lorem in dui. Cras ultricies mi eu turpis hendrerit fringilla. Vestibulum ante ipsum primis in faucibus orci luctus et ultrices posuere cubilia curae.</p>
  <p style="position:absolute;left:550px;top:92px;width:230px;color:#c7c7cd">Phasellus tempus. Proin viverra, ligula sit amet ultrices semper, ligula arcu tristique sapien, a accumsan nisi mauris ac eros. Donec vitae sapien ut libero venenatis faucibus. Nullam quis ante. Etiam sit amet orci eget eros faucibus tincidunt. Duis leo. Sed fringilla mauris sit amet nibh. Donec sodales sagittis magna. Sed consequat, leo eget bibendum sodales, augue velit cursus nunc, quis gravida magna mi a libero. Fusce vulputate eleifend sapien. Vestibulum purus quam, scelerisque ut, mollis sed.</p>
  <p style="position:absolute;left:24px;top:258px;width:760px;color:#c7c7cd">Phasellus tempus. Proin viverra, ligula sit amet ultrices semper, ligula arcu tristique sapien, a accumsan nisi mauris ac eros. Fusce neque. Quisque id mi. Ut tincidunt tincidunt erat. Etiam feugiat lorem non metus. Vestibulum dapibus nunc ac augue. Curabitur vestibulum aliquam leo. Praesent egestas neque eu enim. In hac habitasse platea dictumst. Fusce a quam. Etiam ut purus mattis mauris sodales aliquam. Curabitur nisi. Quisque malesuada placerat nisl. Nam ipsum risus, rutrum vitae, vestibulum eu, molestie vel, lacus. Sed augue ipsum, egestas nec, vestibulum et, malesuada adipiscing, dui. Vestibulum facilisis, purus nec pulvinar iaculis, ligula mi congue nunc, vitae euismod ligula urna in dolor.</p>
  <p style="position:absolute;left:24px;top:362px;width:760px;color:#9a9aa2;font-style:italic">Praesent ac massa at ligula laoreet iaculis. Nulla neque dolor, sagittis eget, iaculis quis, molestie non, velit. Mauris turpis nunc, blandit et, volutpat molestie, porta ut, ligula. Fusce pharetra convallis urna.</p>
  <div class="stat" style="left:24px"><span></span>1 189 185</div>
  <div class="stat" style="left:184px"><span></span>1 168 489</div>
  <div class="stat" style="left:344px"><span></span>4 210 568</div>
  <div class="stat" style="left:504px"><span></span>2 148 984</div>
  <div class="stat" style="left:664px"><span></span>4 189 498</div>
</section>

<article class="card rcard" style="left:800px;top:2599px;width:400px;height:518px">
  <div class="ph" style="left:14px;top:8px;width:372px;height:272px;background:linear-gradient(135deg,#5a6070,#2c3038 60%,#8a7060)" role="img" aria-label="Two police officers by a wall"></div>
  <p style="position:absolute;left:16px;top:296px;width:368px;color:#555"><span class="dropcap">P</span>raesent adipiscing. Phasellus ullamcorper ipsum rutrum nunc. Nunc nonummy metus. Vestibulum volutpat pretium libero. Cras id dui. Aenean ut eros et nisl sagittis vestibulum. Nullam nulla eros, ultricies sit amet, nonummy id, imperdiet feugiat, pede. Sed lectus. Donec mollis hendrerit risus. Phasellus nec sem in justo pellentesque facilisis. Etiam imperdiet imperdiet orci. Nunc nec neque. Phasellus leo dolor, tempus non, auctor et, hendrerit quis, nisi. Curabitur ligula sapien, tincidunt non, euismod vitae, posuere imperdiet, leo. Maecenas malesuada.</p>
  <p style="position:absolute;left:16px;top:420px;width:368px;color:#555">Donec posuere vulputate arcu. Phasellus accumsan cursus velit. Vestibulum ante ipsum primis in faucibus orci luctus et ultrices posuere cubilia curae. Sed aliquam, nisi quis porttitor congue, elit erat euismod orci, ac placerat dolor lectus quis orci. Curabitur turpis nunc, blandit et, volutpat molestie, porta ut, ligula.</p>
</article>

<section class="abs special">
  <div class="lbl">Special<br>projects</div>
  <div class="item" style="left:100px">World Humanitarian Day: voices from the field revisited</div>
  <div class="item" style="left:380px;background:linear-gradient(90deg,#4a4a52,#2a2a30)" role="img" aria-label="Newsroom background">Breaking news on 2016 year and interview with…</div>
  <div class="item" style="left:650px">Fortuna billionaires: full list of the richest people in the world</div>
  <div class="item" style="left:930px">Most top places and the best apartments with Staynest service</div>
</section>

<footer class="abs footer">
  <div class="fcol" style="left:14px"><h4>News</h4><a>Politics</a><a class="on">Sports</a><a>Money</a><a>World</a></div>
  <div class="fcol" style="left:112px"><h4>Sports</h4><a>PFL</a><a>PBL</a><a>PBA</a><a>PHL</a><a>Golf</a><a>CFA</a><a>CBA</a></div>
  <div class="fcol" style="left:212px"><h4>Life</h4><a>People</a><a>Movies</a><a>Music</a><a>TV</a><a>Books</a></div>
  <div class="fcol" style="left:310px"><h4>Money</h4><a>Markets</a><a>Business</a><a>Personal Finance</a><a>Cars</a><a>Careers</a></div>
  <div class="fcol" style="left:410px"><h4>Tech</h4><a>Politics</a><a>Sports</a><a>Money</a><a>World</a></div>
  <div class="fcol" style="left:510px"><h4>Politics</h4><a>Australia</a><a>Canada</a><a>France</a><a>Germany</a><a>Poland</a><a>Ukraine</a></div>
  <div class="fcol" style="left:610px"><h4>Travel</h4><a>Business Travel</a><a>Experience Travel</a><a>Destinations</a><a>Flights</a><a>Cruises</a><a>Deals</a></div>
  <div class="fcol" style="left:710px"><h4>Opinion</h4><a>FQJ</a><a>HVZ</a><a>Fortuna</a></div>
  <div class="fcol" style="left:810px"><h4>Investing</h4><a>Our Website</a><a>Charity</a><a>Business</a><a>Help Center</a><a>Contact Us</a></div>
  <div class="fcol" style="left:910px"><h4>Lifestyle</h4><a>Freelance</a><a>Travel</a><a>Sport</a><a>Money</a></div>
  <div class="fcol" style="left:1010px"><h4>Business</h4><a>Ideas</a><a>Investors</a><a>Offers</a></div>
  <div class="fcol" style="left:1110px"><h4>Video</h4><a>News</a><a>World</a><a>Politics</a><a>Media</a><a>Have You Seen</a></div>
</footer>
<div class="abs bottombar">
  <div class="logo" style="height:32px;line-height:32px;font-size:14px;width:70px">LOGO</div>
  <div class="follow" style="line-height:32px;font-size:10px;color:#aaa;left:86px">Follow Us <span class="dot"></span><span class="dot red"></span><span class="dot"></span><span class="dot"></span><span class="dot"></span></div>
</div>

</body>
</html>
```